Zielgruppe
Einzelnfirmen, Arbeitsgruppen und KMU im Dienstleistungssektor.
Aufgabenstellung
Vorweg: Dem Auftrag folgen weitere Teilaufträge an den Gewinner, natürlich gegen Bezahlung.
Für die bereits programmierte Webapplikation "tallo" wird ein Design benötigt. Tallo ähnelt den bereits bestehenden Zeiterfassungssystemen, soll sich aber anhand von Einfachheit, Speditivität und grafischer Eleganz von anderen abheben. Zudem sind Features geplant, die in anderen Systemen nicht oder nur mangelhaft implementiert sind.
Was benötigt wird:
1) Ein Log-In im Splashscreen-Style. Siehe Linkbox mit Beispiel. Das Login hebt sich vom Hauptdesign ab.
Elemente, die beim Login vorhanden sind: Email- und Passwortfeld, Passwort vergessen Link, Platz für das Logo des Accountinhabers (Firmenlogo o.ä).
Zum Logo des Accountinhabers: Wenn der Inhaber keines Hochgeladen hat soll das Login so angezeigt werden wie wenn kein Platz für ein Logo da wäre. Dies muss aber nicht separat nochmals als Design hochgeladen werden, es reicht mir eine Version mit einem Logo. Als Logo kann beispielsweise das Firmenlogo von ravelmark verwendet werden.
2) Das Hauptdesign, welches für die Webapplikation gilt. Also für alles andere ausser das Login. Hier ist beispielsweise die Navigation vorhanden und eine kleine Version vom tallo logo. In das Hauptdesign werden alle weiteren Inhalte der Applikation integriert (Projektliste, Zeiterfassung, Benutzer-Management, Statistiken, Abrechnungen, ...).
Für den Beispielinhalt hätte ich gern eine simple Liste/Tabelle, beispielsweise von Systembenutzern oder Projekten und kein Lorem Ipsum.
Für mich ist es relativ schwer, alles zu beschreiben, da ich von Anfang an bei tallo mitgearbeitet habe und dort mitten drin bin. Fragen sind also sehr willkommen und werden ausführlich beantwortet!

```html
<!DOCTYPE html>
<html lang="de">
<head>
<meta charset="utf-8">
<title>Tallo – Projekte</title>
<link href="https://fonts.googleapis.com/css2?family=Arimo:wght@400;700&display=swap" rel="stylesheet">
<style>
:root{
  --blue-dark:#0a68a8;
  --blue:#1488d0;
  --blue-light:#22a3e8;
  --link:#1a8fd6;
  --text:#666;
  --text-dark:#555;
  --row:#f8f8f8;
  --line:#e2e2e2;
  --nav-top:#fbfbfb;
  --nav-bottom:#dcdcdc;
  --footer:#ececec;
  --red:#c0392b;
  --orange:#d98a0b;
  --green:#7aa51a;
  --bar-bg:#dedede;
}
*{box-sizing:border-box;margin:0;padding:0}
html,body{width:1200px;height:1200px;overflow:hidden;background:#fff}
body{font-family:"Arimo",Arial,sans-serif;color:var(--text)}
.canvas{width:1200px;height:1200px;overflow:hidden;position:relative}
.stage{width:1024px;height:1024px;position:absolute;top:0;left:0;transform:scale(1.171875);transform-origin:0 0}

/* header */
.site-header{position:absolute;left:0;top:0;width:1024px;height:100px;background:linear-gradient(180deg,var(--blue-dark),var(--blue) 70%,var(--blue-light))}
.brand{position:absolute;display:flex;align-items:center;gap:8px;font-size:28px;font-weight:700;line-height:1;white-space:nowrap}
.brand-square{width:14px;height:14px;background:currentColor}
.site-header .brand{left:186px;top:50px;color:#fff}
.account{position:absolute;left:762px;top:26px;display:flex;height:21px}
.btn{display:flex;align-items:center;gap:5px;font-size:9.5px;font-weight:700;padding:0 7px;border-radius:4px;white-space:nowrap}
.btn-account{background:linear-gradient(#fff,#d9d9d9);color:#444;border:1px solid #bbb;width:94px}
.btn-logout{background:linear-gradient(#1fa0ea,#0b74be);color:#fff;width:66px;margin-left:-2px}

/* nav */
.main-nav{position:absolute;left:0;top:100px;width:1024px;height:40px;background:linear-gradient(var(--nav-top),var(--nav-bottom));border-top:1px solid #fff;border-bottom:1px solid #c8c8c8}
.nav-item{position:absolute;top:0;height:39px;display:flex;align-items:center;gap:7px;padding-left:14px;font-size:11px;font-weight:700;color:#555;border-left:1px solid #c9c9c9;white-space:nowrap}
.nav-item.is-active{background:#fff;color:var(--link)}
.nav-item.is-active::before{content:"";position:absolute;left:50%;top:-1px;margin-left:-6px;border:6px solid transparent;border-top-color:var(--blue-light)}
.search{position:absolute;left:724px;top:0;width:205px;height:39px;border-left:1px solid #c9c9c9;border-right:1px solid #c9c9c9}
.search-field{position:absolute;left:17px;top:8px;width:175px;height:25px;background:#fff;border:1px solid #ccc;border-radius:4px;font-size:10px;color:#999;padding:7px 8px}
.search-btn{position:absolute;left:164px;top:10px;width:27px;height:21px;border-radius:3px;background:linear-gradient(#d8d8d8,#9a9a9a);display:flex;align-items:center;justify-content:center}

/* content */
.page-title{position:absolute;left:105px;top:175px;font-size:11px;font-weight:700;color:var(--text-dark)}
.project-table{position:absolute;left:96px;top:213px;width:833px;border-collapse:collapse;font-size:10px;table-layout:fixed}
.project-table th{height:33px;background:linear-gradient(#27a8ec,#0d78c2);color:#fff;font-weight:700;text-align:left;padding-left:8px;border-right:1px solid #0d6aac}
.project-table td{height:33.3px;background:var(--row);border-right:1px solid var(--line);border-bottom:1px dotted #ddd;padding-left:8px;color:var(--text);white-space:nowrap}
.project-table td.num{text-align:right;padding-right:10px}
.budget{display:flex;align-items:center}
.budget-amount{width:48px;text-align:right}
.bar{margin-left:12px;width:99px;height:14px;background:var(--bar-bg);border:1px solid #c6c6c6}
.bar-fill{display:block;height:100%}
.fill-low{background:linear-gradient(#c9dd26,#9fba0c)}
.fill-mid{background:linear-gradient(90deg,#b2cc12,#e9a828)}
.fill-high{background:linear-gradient(90deg,#b2cc12,#eeaa2c 60%,#f69b9b)}
.project-table td.st-red{color:var(--red)}
.project-table td.st-orange{color:var(--orange)}
.project-table td.st-green{color:var(--green)}

/* footer */
.site-footer{position:absolute;left:0;top:684px;width:1024px;height:133px;background:var(--footer)}
.footer-col{position:absolute;top:22px;list-style:none;font-size:10px;line-height:19px}
.footer-col a{color:var(--link);text-decoration:none}
.site-footer .brand{right:116px;top:34px;color:var(--link)}
.copyright{position:absolute;left:710px;top:76px;font-size:9.5px;color:#999}
</style>
</head>
<body>
<div class="canvas">
<div class="stage">

<header class="site-header">
  <div class="brand"><span class="brand-square"></span>Tallo</div>
  <div class="account">
    <span class="btn btn-account">
      <svg width="12" height="12" viewBox="0 0 12 12"><circle cx="6" cy="4" r="2.6" fill="#e7a15a"/><path d="M1 12c0-3 2-5 5-5s5 2 5 5z" fill="#5aa640"/></svg>
      Mein Account
    </span>
    <span class="btn btn-logout">
      <svg width="12" height="12" viewBox="0 0 12 12"><circle cx="6" cy="6" r="5.5" fill="#e0282c"/><rect x="3" y="5" width="6" height="2" fill="#fff"/></svg>
      Logout
    </span>
  </div>
</header>

<nav class="main-nav">
  <span class="nav-item" style="left:96px;width:111px">
    <svg width="15" height="13" viewBox="0 0 15 13"><path d="M1 7L7.5 1 14 7" stroke="#d33" stroke-width="2" fill="none"/><rect x="3.5" y="6.5" width="8" height="6" fill="#f2e7d0" stroke="#b59966"/></svg>Dashboard</span>
  <span class="nav-item is-active" style="left:207px;width:96px">
    <svg width="14" height="14" viewBox="0 0 14 14"><rect x="1" y="3" width="9" height="10" fill="#fff" stroke="#999"/><path d="M5 10l1-3 6-6 2 2-6 6z" fill="#f0a030"/></svg>Projekte</span>
  <span class="nav-item" style="left:303px;width:126px">
    <svg width="14" height="14" viewBox="0 0 14 14"><circle cx="7" cy="7" r="6.5" fill="#e98a1a"/><circle cx="7" cy="7" r="4" fill="#fff"/><path d="M7 4.5V7l2 1" stroke="#e98a1a" fill="none"/></svg>Zeiterfassung</span>
  <span class="nav-item" style="left:429px;width:112px">
    <svg width="14" height="15" viewBox="0 0 14 15"><rect x="1.5" y="1" width="10" height="13" fill="#fff" stroke="#889"/><path d="M4 5h5M4 8h5M4 11h3" stroke="#88a"/><circle cx="10" cy="11" r="2.5" fill="none" stroke="#d55"/></svg>Controlling</span>
  <span class="nav-item" style="left:541px;width:106px">
    <svg width="16" height="13" viewBox="0 0 16 13"><circle cx="5" cy="3.5" r="2.5" fill="#e8a35c"/><circle cx="11" cy="3.5" r="2.5" fill="#e8a35c"/><path d="M0 13c0-4 2-6 5-6s5 2 5 6z" fill="#3d7fd0"/><path d="M6 13c0-4 2-6 5-6s5 2 5 6z" fill="#d34a4a"/></svg>Benutzer</span>
  <span class="nav-item" style="left:647px;width:77px">
    <svg width="14" height="14" viewBox="0 0 14 14"><circle cx="7" cy="7" r="6.5" fill="#1d8fd8"/><text x="7" y="10.5" font-size="10" font-weight="700" text-anchor="middle" fill="#fff" font-family="Arimo,Arial,sans-serif">?</text></svg>Hilfe</span>
  <div class="search">
    <div class="search-field">Suchbegriff eingeben...</div>
    <span class="search-btn"><svg width="11" height="11" viewBox="0 0 11 11"><circle cx="4.5" cy="4.5" r="3.2" fill="none" stroke="#444" stroke-width="1.4"/><path d="M7 7l3 3" stroke="#444" stroke-width="1.6"/></svg></span>
  </div>
</nav>

<main>
  <h1 class="page-title">Alle Projekte im Überblick</h1>
  <table class="project-table">
    <colgroup>
      <col style="width:142px"><col style="width:179px"><col style="width:59px"><col style="width:136px"><col style="width:135px"><col style="width:81px"><col style="width:101px">
    </colgroup>
    <thead>
      <tr><th>Projekt</th><th>Budget</th><th>Stunden</th><th>Dienstleister</th><th>Status</th><th>Projektende</th><th>Archiviert</th></tr>
    </thead>
    <tbody>
      <tr><td>Name des Projektes</td><td><div class="budget"><span class="budget-amount">18.000€</span><span class="bar"><span class="bar-fill fill-low" style="width:55%"></span></span></div></td><td class="num">40 h</td><td>3 Firmen / 5 Arbeiter</td><td>In Arbeit</td><td>24.12.2010</td><td>nicht archiviert</td></tr>
      <tr><td>Name des Projektes</td><td><div class="budget"><span class="budget-amount">40.000€</span><span class="bar"><span class="bar-fill fill-low" style="width:28%"></span></span></div></td><td class="num">74 h</td><td>3 Firmen / 5 Arbeiter</td><td>In Arbeit</td><td>24.12.2010</td><td>nicht archiviert</td></tr>
      <tr><td>Name des Projektes</td><td><div class="budget"><span class="budget-amount">10.000€</span><span class="bar"><span class="bar-fill fill-low" style="width:28%"></span></span></div></td><td class="num">25 h</td><td>3 Firmen / 5 Arbeiter</td><td class="st-red">Abgeschlossen</td><td class="st-red">Beendet</td><td class="st-red">Archiviert</td></tr>
      <tr><td>Name des Projektes</td><td><div class="budget"><span class="budget-amount">5.000€</span><span class="bar"><span class="bar-fill fill-mid" style="width:82%"></span></span></div></td><td class="num">10 h</td><td>3 Firmen / 5 Arbeiter</td><td>In Arbeit</td><td>24.12.2010</td><td>nicht archiviert</td></tr>
      <tr><td>Name des Projektes</td><td><div class="budget"><span class="budget-amount">20.000€</span><span class="bar"><span class="bar-fill fill-mid" style="width:93%"></span></span></div></td><td class="num">35 h</td><td>3 Firmen / 5 Arbeiter</td><td class="st-orange">Rechnung erstellt</td><td class="st-red">Beendet</td><td class="st-red">Archiviert</td></tr>
      <tr><td>Name des Projektes</td><td><div class="budget"><span class="budget-amount">80.000€</span><span class="bar"><span class="bar-fill fill-high" style="width:100%"></span></span></div></td><td class="num">100 h</td><td>3 Firmen / 5 Arbeiter</td><td>In Arbeit</td><td>24.12.2010</td><td>nicht archiviert</td></tr>
      <tr><td>Name des Projektes</td><td><div class="budget"><span class="budget-amount">6.000€</span><span class="bar"><span class="bar-fill fill-low" style="width:17%"></span></span></div></td><td class="num">12 h</td><td>3 Firmen / 5 Arbeiter</td><td class="st-green">Rechnung bezahlt</td><td class="st-red">Beendet</td><td class="st-red">Archiviert</td></tr>
      <tr><td>Name des Projektes</td><td><div class="budget"><span class="budget-amount">100.000€</span><span class="bar"><span class="bar-fill fill-low" style="width:43%"></span></span></div></td><td class="num">150 h</td><td>3 Firmen / 5 Arbeiter</td><td>In Arbeit</td><td>24.12.2010</td><td>nicht archiviert</td></tr>
      <tr><td>Name des Projektes</td><td><div class="budget"><span class="budget-amount">25.000€</span><span class="bar"><span class="bar-fill fill-mid" style="width:70%"></span></span></div></td><td class="num">37 h</td><td>3 Firmen / 5 Arbeiter</td><td>In Arbeit</td><td>24.12.2010</td><td>nicht archiviert</td></tr>
      <tr><td>Name des Projektes</td><td><div class="budget"><span class="budget-amount">60.000€</span><span class="bar"><span class="bar-fill fill-mid" style="width:90%"></span></span></div></td><td class="num">80 h</td><td>3 Firmen / 5 Arbeiter</td><td class="st-red">Abgeschlossen</td><td class="st-red">Beendet</td><td class="st-red">Archiviert</td></tr>
      <tr><td>Name des Projektes</td><td><div class="budget"><span class="budget-amount">12.000€</span><span class="bar"><span class="bar-fill fill-high" style="width:100%"></span></span></div></td><td class="num">27 h</td><td>3 Firmen / 5 Arbeiter</td><td>In Arbeit</td><td>24.12.2010</td><td>nicht archiviert</td></tr>
      <tr><td>Name des Projektes</td><td><div class="budget"><span class="budget-amount">75.000€</span><span class="bar"><span class="bar-fill fill-mid" style="width:69%"></span></span></div></td><td class="num">90 h</td><td>3 Firmen / 5 Arbeiter</td><td class="st-orange">Rechnung erstellt</td><td class="st-red">Beendet</td><td class="st-red">Archiviert</td></tr>
    </tbody>
  </table>
</main>

<footer class="site-footer">
  <ul class="footer-col" style="left:105px"><li><a href="#">Dashboard</a></li><li><a href="#">Projekte</a></li><li><a href="#">Zeiterfassung</a></li><li><a href="#">Controlling</a></li><li><a href="#">Benutzer</a></li></ul>
  <ul class="footer-col" style="left:249px"><li><a href="#">Mein Accout</a></li><li><a href="#">Hilfe</a></li><li><a href="#">Disclaimer</a></li><li><a href="#">AGB</a></li><li><a href="#">Logout</a></li></ul>
  <ul class="footer-col" style="left:412px"><li><a href="#">Kontakt</a></li><li><a href="#">Impressum</a></li><li><a href="#">Feedback</a></li></ul>
  <div class="brand"><span class="brand-square"></span>Tallo</div>
  <p class="copyright">© 2010 Tallo.de - Alle Rechte vorbehalten</p>
</footer>

</div>
</div>
</body>
</html>
```